Playvora Print Ad Design

Need a newspaper ad of size 24 cm H X 16 cm W for my toy rental library- Playvora

Toy Libraries are a new concept in India & so consumers need to be introduced to this concept through the ad.

The ad should communicate the following things

1. Why buy toys when you can rent a new one every week?
2. Our large collection of toys, games & puzzles (1000+ items)
3. Our collection is based on the Multiple Intelligence Theory of Dr. Felix Ormond which says there are 8 intelligence areas.
4. Customers have the convenience of ordering online & getting home delivery or they could simply walk into to our library to borrow toys.

Please check our website www.playvora-example.in for more details of our service.

Kunal

Target Market(s)

Parents of children in the age group 1 year - 7 years

Industry/Entity Type

Library

Requirements
Must have
• Photos or icons of toys, children playing etc

Different icons depicting the 8 intelligence areas

Our physical address
2nd Floor, 517 Maple Arcade, Opp Sunvale Bazaar
Zenora Phase-2, Gurgaon-122918

```html
<!DOCTYPE html>
<html lang="en">
<head>
<meta charset="utf-8">
<title>Playvora – Toy Rental Library</title>
<link href="https://fonts.googleapis.com/css2?family=Nunito:wght@400;600;700;800;900&family=Oswald:wght@600;700&display=swap" rel="stylesheet">
<style>
  :root {
    --sky-top: #d9f1fb;
    --sky-bottom: #eaf7fd;
    --white: #ffffff;
    --purple: #5b2a86;
    --purple-band: #4f2a82;
    --teal: #1aa6b7;
    --magenta: #d81b5d;
    --orange: #f39a1e;
    --green: #4a9a2c;
    --ink: #3a2b55;
    --toy-warm: #e7b76a;
    --toy-cool: #9ccfd6;
  }
  * { margin: 0; padding: 0; box-sizing: border-box; }
  html, body { width: 800px; height: 1200px; overflow: hidden; }
  body { font-family: "Nunito", sans-serif; background: var(--white); }

  .ad {
    position: relative;
    width: 800px; height: 1200px;
    overflow: hidden;
    background: linear-gradient(180deg, var(--sky-top), var(--sky-bottom) 60%, var(--white));
  }

  .header-wave { position: absolute; top: 0; left: 0; width: 800px; height: 270px; }

  .brand {
    position: absolute; top: 24px; left: 60px;
    display: flex; align-items: center; gap: 24px;
  }
  .brand-mark {
    width: 104px; height: 104px; border-radius: 50%;
    background: var(--purple);
  }
  .brand-text { display: flex; flex-direction: column; }
  .brand-name {
    font-weight: 800; font-size: 72px; line-height: 0.95;
    color: var(--purple); letter-spacing: 1px;
  }
  .brand-tagline {
    font-weight: 700; font-size: 42px; line-height: 1.1;
    color: var(--teal);
  }
  .brand-theory {
    position: absolute; top: 166px; left: 150px;
    font-weight: 700; font-size: 30px; color: var(--purple);
    white-space: nowrap;
  }

  .headline {
    position: absolute; top: 272px; left: 24px;
    width: 580px;
    transform: rotate(-6deg); transform-origin: left top;
    text-align: center;
  }
  .headline-lead {
    display: block;
    font-weight: 800; font-size: 40px; line-height: 46px; color: var(--teal);
  }
  .headline-punch {
    display: block;
    font-family: "Oswald", sans-serif; font-weight: 700;
    font-size: 66px; line-height: 76px; color: var(--magenta);
    letter-spacing: 1px;
  }

  .count-badge {
    position: absolute; top: 236px; left: 622px;
    width: 158px; height: 158px; border-radius: 50%;
    background: var(--orange); color: var(--white);
    display: flex; flex-direction: column; align-items: center; justify-content: center;
    font-weight: 900; line-height: 1;
    transform: rotate(-10deg);
  }
  .count-number { font-size: 46px; }
  .count-label { font-size: 32px; }

  .toy-photo {
    position: absolute; top: 446px; left: 16px;
    width: 384px; height: 258px; border-radius: 10px;
    background: linear-gradient(135deg, var(--toy-cool), var(--toy-warm) 55%, #f3dca8);
  }

  .collection-note {
    position: absolute; top: 460px; left: 420px; width: 370px;
    font-weight: 700; font-size: 38px; line-height: 1.18; color: var(--orange);
  }

  .theory-band {
    position: absolute; top: 716px; left: 0; width: 800px; height: 68px;
    background: var(--purple-band); color: var(--white);
    padding: 8px 24px; font-weight: 700; font-size: 20px; line-height: 26px;
    white-space: nowrap;
  }

  .intelligences { position: absolute; top: 796px; left: 20px; width: 400px; }
  .section-title {
    font-weight: 900; font-size: 27px; line-height: 34px; color: var(--green);
    letter-spacing: 0.5px; white-space: nowrap;
  }
  .intelligence-grid { position: relative; margin-top: 12px; height: 196px; }
  .intelligence-list {
    list-style: none; position: absolute; top: 2px; left: 50px; width: 290px;
    text-align: center;
  }
  .intelligence-list li {
    font-weight: 800; font-size: 20px; line-height: 24px; color: var(--ink);
    white-space: nowrap;
  }
  .area-icon {
    position: absolute; width: 38px; height: 38px; border-radius: 8px;
  }

  .borrow { position: absolute; top: 796px; left: 440px; width: 350px; }
  .borrow .section-title { font-size: 32px; line-height: 40px; }
  .borrow-list { list-style: none; margin-top: 6px; }
  .borrow-list li {
    font-weight: 800; font-size: 18px; line-height: 28px; color: var(--purple);
    text-transform: uppercase; white-space: nowrap;
  }
  .borrow-list li::before { content: "• "; }

  .address-box {
    position: absolute; top: 952px; left: 440px; width: 345px; height: 112px;
    background: var(--purple-band); color: var(--white);
    padding: 12px 16px; font-style: normal;
    font-weight: 700; font-size: 19px; line-height: 29px;
    white-space: nowrap; text-align: center;
  }
</style>
</head>
<body>
<main class="ad">
  <svg class="header-wave" viewBox="0 0 800 270" aria-hidden="true">
    <path d="M0 0 H800 V232 C680 196 560 270 400 246 C260 224 140 270 0 230 Z" fill="#ffffff"/>
  </svg>

  <header class="brand">
    <div class="brand-mark" aria-hidden="true"></div>
    <div class="brand-text">
      <span class="brand-name">Playvora</span>
      <span class="brand-tagline">Toy Rental Library</span>
    </div>
  </header>
  <p class="brand-theory">Based on Multiple Intelligence Theory</p>

  <h1 class="headline">
    <span class="headline-lead">Why buy toys when<br>you can rent a new one</span>
    <span class="headline-punch">EVERY WEEK?</span>
  </h1>

  <div class="count-badge">
    <span class="count-number">1000+</span>
    <span class="count-label">items!</span>
  </div>

  <div class="toy-photo" role="img" aria-label="Wooden educational toys: a pull-along walker, a xylophone pounding bench, shape sorters and picture puzzles"></div>

  <p class="collection-note">We have a large collection of toys, games &amp; puzzles</p>

  <p class="theory-band">Our collection is based on the Multiple Intelligence Theory of<br>Dr. Felix Ormond which says there are intelligence areas.</p>

  <section class="intelligences">
    <h2 class="section-title">DIFFERENT INTELLIGENCES</h2>
    <div class="intelligence-grid">
      <span class="area-icon" style="top:4px;left:0;background:#2f6fb5" role="img" aria-label="Book icon"></span>
      <span class="area-icon" style="top:4px;left:340px;background:#3a9a3a" role="img" aria-label="Numbers icon"></span>
      <span class="area-icon" style="top:52px;left:0;background:#d8322c" role="img" aria-label="Hand icon"></span>
      <span class="area-icon" style="top:52px;left:340px;background:#2d9a6e" role="img" aria-label="Music notes icon"></span>
      <span class="area-icon" style="top:100px;left:0;background:#e88a1a" role="img" aria-label="People icon"></span>
      <span class="area-icon" style="top:100px;left:340px;background:#e3b21a" role="img" aria-label="Person icon"></span>
      <span class="area-icon" style="top:148px;left:0;background:#2e8b2e" role="img" aria-label="Leaf icon"></span>
      <span class="area-icon" style="top:148px;left:340px;background:#e9821b" role="img" aria-label="Eye icon"></span>
      <ul class="intelligence-list">
        <li>Linguistic</li>
        <li>Logical-mathematical</li>
        <li>Bodily-Kinesthetic</li>
        <li>Musical</li>
        <li>Interpersonal</li>
        <li>Intrapersonal</li>
        <li>Naturalist</li>
        <li>Spatial</li>
      </ul>
    </div>
  </section>

  <section class="borrow">
    <h2 class="section-title">BORROW OUR TOYS</h2>
    <ul class="borrow-list">
      <li>Ordering online</li>
      <li>Getting home delivery</li>
      <li>Walking in into our library</li>
    </ul>
  </section>

  <address class="address-box">
    2nd Floor, 517 Maple Arcade,<br>
    Opp Sunvale Bazaar<br>
    Zenora Phase-2, Gurgaon-122918
  </address>
</main>
</body>
</html>
```